Real Estate Business Cards

Looking for a clean, sharp and professional look for our Real Estate investment Fund that invests in Multi Family Apartment buildings.

Target Market(s)

Real Estate Fund

Industry/Entity Type

Real Estate

Contact Information for Business Card

Company Description: Real Estate Investment Fund
Company Name: RKW Holdings
Name: Marcus Olvane
Cell: (917) 482-0657
Email: marcus@rkwholdings-example.com
Website: www.rkwholdings-example.com
Address: 418, 9th Street, Brooklyn NY 11218

Colors

Designer to choose colors to be used in the design.

Requirements
Nice to have
• Colors to match logo

```html
<!DOCTYPE html>
<html lang="en">
<head>
<meta charset="utf-8">
<title>RKW Holdings – Business Cards</title>
<link rel="stylesheet" href="https://fonts.googleapis.com/css2?family=Cinzel:wght@400;500&family=Poppins:wght@300;400&display=swap">
<style>
  :root {
    --bg: #e9eaec;
    --card: #ffffff;
    --brand-blue: #1c6aa8;
    --charcoal: #3d4044;
    --text-grey: #55585c;
    --rule: #9a9da1;
  }
  * { box-sizing: border-box; margin: 0; padding: 0; }
  html, body { width: 1200px; height: 960px; overflow: hidden; }
  body {
    background: var(--bg);
    font-family: "Poppins", sans-serif;
    display: flex;
    flex-direction: column;
    align-items: center;
    justify-content: center;
    gap: 40px;
  }
  .card {
    position: relative;
    width: 720px;
    height: 412px;
    background: var(--card);
    box-shadow: 0 6px 18px rgba(0,0,0,0.12);
    overflow: hidden;
  }

  /* Brand lockup: plain square + name */
  .brand { display: flex; align-items: center; gap: 16px; }
  .brand-square { width: 46px; height: 46px; background: var(--brand-blue); }
  .brand-name {
    font-family: "Cinzel", serif;
    font-weight: 400;
    color: var(--brand-blue);
    letter-spacing: 1px;
    white-space: nowrap;
  }

  /* Front */
  .card-front {
    display: flex;
    flex-direction: column;
    align-items: center;
    justify-content: center;
  }
  .card-front .brand { flex-direction: column; gap: 22px; }
  .card-front .brand-square { width: 70px; height: 70px; }
  .card-front .brand-name { font-size: 40px; }
  .front-web {
    margin-top: 48px;
    font-size: 14px;
    letter-spacing: 7px;
    color: var(--charcoal);
  }
  .front-web .accent { color: var(--brand-blue); }

  /* Back */
  .card-back .brand {
    position: absolute;
    top: 58px;
    left: 50%;
    transform: translateX(-50%);
  }
  .card-back .brand-name { font-size: 32px; }
  .back-rule {
    position: absolute;
    left: 44px;
    right: 40px;
    top: 232px;
    height: 1px;
    background: var(--rule);
  }
  .holder-name {
    position: absolute;
    left: 44px;
    top: 190px;
    font-family: "Cinzel", serif;
    font-size: 28px;
    color: var(--brand-blue);
    letter-spacing: 0.5px;
  }
  .contact-list {
    position: absolute;
    left: 44px;
    top: 248px;
    list-style: none;
    font-size: 17px;
    font-weight: 300;
    color: var(--text-grey);
    line-height: 27px;
  }
  .contact-list li { display: flex; align-items: center; gap: 10px; }
  .contact-list svg { width: 15px; height: 15px; flex: none; }
  .address {
    position: absolute;
    right: 40px;
    top: 246px;
    text-align: right;
    font-size: 16px;
    font-weight: 300;
    color: var(--text-grey);
    line-height: 24px;
  }
  .band-dark {
    position: absolute;
    left: 0; right: 0; bottom: 26px;
    height: 6px;
    background: var(--charcoal);
  }
  .band-blue {
    position: absolute;
    left: 0; right: 0; bottom: 0;
    height: 26px;
    background: var(--brand-blue);
  }
</style>
</head>
<body>

  <section class="card card-front">
    <div class="brand">
      <div class="brand-square"></div>
      <div class="brand-name">RKW HOLDINGS</div>
    </div>
    <div class="front-web">www.<span class="accent">rkwholdings-example</span>.com</div>
  </section>

  <section class="card card-back">
    <div class="brand">
      <div class="brand-square"></div>
      <div class="brand-name">RKW HOLDINGS</div>
    </div>

    <div class="holder-name">Marcus Olvane</div>
    <div class="back-rule"></div>

    <ul class="contact-list">
      <li>
        <svg viewBox="0 0 16 16" aria-hidden="true"><rect x="4" y="1" width="8" height="14" rx="1.5" fill="none" stroke="var(--charcoal)" stroke-width="1.6"/></svg>
        (917) 482-0657
      </li>
      <li>
        <svg viewBox="0 0 16 16" aria-hidden="true"><rect x="1" y="3" width="14" height="10" fill="var(--brand-blue)"/><path d="M1 3 L8 9 L15 3" fill="none" stroke="#fff" stroke-width="1.3"/></svg>
        marcus@rkwholdings-example.com
      </li>
      <li>
        <svg viewBox="0 0 16 16" aria-hidden="true"><circle cx="8" cy="8" r="7" fill="var(--brand-blue)"/><path d="M1 8 H15 M8 1 C4 5 4 11 8 15 M8 1 C12 5 12 11 8 15" fill="none" stroke="#fff" stroke-width="1"/></svg>
        www.rkwholdings-example.com
      </li>
    </ul>

    <div class="address">418, 9th Street<br>Brooklyn NY 11218</div>

    <div class="band-dark"></div>
    <div class="band-blue"></div>
  </section>

</body>
</html>
```